TOLV Van Desgin

Dear All, Thanks for taking our project into your interest. Am looking to have the van full cover with our service and some photos. Our Services: Van Type: brx van dorima 2014 side

Target Market(s)

Commercial and residential cleaning

Industry/Entity Type

Cleaning Service

Font styles to use
Serif
Sans Serif

Colors
9bcb3c
add136
0655a3
3277b5

Requirements
Must have
• Text to be on 3 sides Right , left and backside
Nice to have
• pictures
Should not have
• to many colors

```html
<!DOCTYPE html>
<html lang="en">
<head>
<meta charset="utf-8">
<title>TOLV Van Wrap – Side</title>
<link href="https://fonts.googleapis.com/css2?family=Crimson+Pro:wght@400;600&family=Roboto+Slab:wght@400&display=swap" rel="stylesheet">
<style>
  :root{
    --leaf:#9bcb3c;
    --lime:#add136;
    --sage:#c4dc95;
    --sage-line:#b2cd80;
    --navy:#0655a3;
    --sky:#3277b5;
    --forest:#3e8a2c;
    --ink:#1f2a1a;
    --white:#f1f1ef;
    --glass:#b9bcbd;
    --trim:#2a2a2a;
    --tyre:#1e1e1e;
    --rim:#c9cbcd;
    --rim-dark:#8d9094;
    --paper:#ffffff;
  }
  html,body{margin:0;padding:0;width:1200px;height:792px;overflow:hidden;background:var(--paper);}
  .van-wrap{display:block;width:1200px;height:792px;}
  .body-green{fill:var(--sage);}
  .body-white{fill:var(--white);}
  .band-lime{fill:var(--lime);}
  .band-navy{fill:var(--navy);}
  .outline{fill:none;stroke:#8fa86a;stroke-width:2;}
  .panel-frame{fill:none;stroke:var(--sage-line);stroke-width:2;}
  .window{fill:var(--glass);stroke:var(--trim);stroke-width:6;}
  .trim{fill:var(--trim);}
  .wheel-well{fill:#3a3a3a;}
  .tyre{fill:var(--tyre);}
  .rim{fill:var(--rim);stroke:var(--rim-dark);stroke-width:3;}
  .hub{fill:var(--rim-dark);}
  .hub-cap{fill:#5b5e62;}
  .ground-shadow{fill:#000;opacity:.12;}
  .door-seam{fill:none;stroke:#9aae80;stroke-width:2;}
  .photo-ring{fill:var(--paper);stroke:var(--leaf);stroke-width:6;}
  .brand{font-family:"Crimson Pro",serif;font-weight:600;fill:var(--forest);}
  .company{font-family:"Crimson Pro",serif;font-weight:400;fill:var(--ink);letter-spacing:.5px;}
  .since{font-family:"Crimson Pro",serif;font-size:12px;fill:var(--ink);}
  .service{font-family:"Roboto Slab",serif;font-size:23px;fill:var(--forest);}
  .web{font-family:"Roboto Slab",serif;font-size:24px;fill:var(--forest);}
  .phone{font-family:"Roboto Slab",serif;font-size:17px;fill:var(--forest);}
</style>
</head>
<body>
<svg class="van-wrap" viewBox="0 0 1500 990" xmlns="http://www.w3.org/2000/svg">
  <defs>
    <clipPath id="van-body">
      <path d="M70 470 Q80 440 140 430 L250 410 Q300 330 440 250 L1360 220 Q1395 230 1405 300 L1420 580 L1430 640 L1260 640 A100 100 0 0 0 1055 640 L375 645 A105 105 0 0 0 165 645 L70 645 Z"/>
    </clipPath>
    <linearGradient id="photo-carpet" x1="0" y1="0" x2="1" y2="1"><stop offset="0" stop-color="#7a6a5a"/><stop offset="1" stop-color="#3c3530"/></linearGradient>
    <linearGradient id="photo-window" x1="0" y1="0" x2="1" y2="1"><stop offset="0" stop-color="#e8efe9"/><stop offset="1" stop-color="#8fbf6a"/></linearGradient>
    <linearGradient id="photo-table" x1="0" y1="0" x2="1" y2="1"><stop offset="0" stop-color="#efe6dc"/><stop offset="1" stop-color="#b69a7c"/></linearGradient>
    <clipPath id="c1"><circle cx="705" cy="525" r="50"/></clipPath>
    <clipPath id="c2"><circle cx="855" cy="540" r="60"/></clipPath>
    <clipPath id="c3"><circle cx="1010" cy="492" r="50"/></clipPath>
  </defs>

  <ellipse class="ground-shadow" cx="750" cy="735" rx="680" ry="28"/>

  <g class="wheel-wells">
    <path class="wheel-well" d="M165 645 A105 105 0 0 1 375 645 Z"/>
    <path class="wheel-well" d="M1055 640 A102.5 102.5 0 0 1 1260 640 Z"/>
  </g>

  <g class="van-body" clip-path="url(#van-body)">
    <rect class="body-green" x="0" y="200" width="1500" height="460"/>
    <path class="band-lime" d="M60 590 Q250 470 520 480 Q900 500 1440 385 L1440 660 L60 660 Z"/>
    <path class="body-white" d="M60 610 Q260 500 520 500 Q900 520 1440 420 L1440 660 L60 660 Z"/>
    <path class="band-navy" d="M360 496 Q520 488 700 555 Q860 610 1000 560 Q870 640 720 585 Q560 520 360 496 Z"/>
    <line class="door-seam" x1="355" y1="410" x2="355" y2="645"/>
    <line class="door-seam" x1="630" y1="245" x2="632" y2="645"/>
  </g>
  <path class="outline" d="M70 470 Q80 440 140 430 L250 410 Q300 330 440 250 L1360 220 Q1395 230 1405 300 L1420 580 L1430 640 L1260 640 A100 100 0 0 0 1055 640 L375 645 A105 105 0 0 0 165 645 L70 645 Z"/>

  <g class="wheels">
    <g class="wheel front">
      <circle class="tyre" cx="270" cy="665" r="97"/>
      <circle class="rim" cx="270" cy="665" r="58"/>
      <circle class="hub" cx="270" cy="665" r="26"/>
      <circle class="hub-cap" cx="270" cy="665" r="12"/>
    </g>
    <g class="wheel rear">
      <circle class="tyre" cx="1158" cy="665" r="97"/>
      <circle class="rim" cx="1158" cy="665" r="58"/>
      <circle class="hub" cx="1158" cy="665" r="26"/>
      <circle class="hub-cap" cx="1158" cy="665" r="12"/>
    </g>
  </g>

  <rect class="window" x="440" y="268" width="155" height="140" rx="8"/>
  <rect class="trim" x="38" y="575" width="125" height="60" rx="10"/>
  <rect class="trim" x="1405" y="578" width="58" height="58" rx="10"/>
  <rect x="1385" y="300" width="38" height="85" rx="6" fill="#b8212a"/>
  <rect x="62" y="480" width="60" height="90" rx="8" fill="#2a2a2a"/>
  <rect x="64" y="540" width="50" height="22" rx="3" fill="#e8951e"/>

  <g class="upper-panel">
    <rect class="panel-frame" x="655" y="250" width="710" height="155" rx="12"/>
    <line class="panel-frame" x1="998" y1="252" x2="1010" y2="403"/>
    <text class="brand" x="820" y="306" font-size="50" text-anchor="middle">TOLV</text>
    <text class="company" x="822" y="360" font-size="23" text-anchor="middle">TOLV CLEANING Co.</text>
    <line x1="783" y1="378" x2="857" y2="376" stroke="var(--ink)" stroke-width="1.2"/>
    <text class="since" x="820" y="391" text-anchor="middle">Since 1989</text>
    <text class="service" x="1070" y="286">General Cleaning</text>
    <text class="service" x="1070" y="316">Window Cleaning</text>
    <text class="service" x="1072" y="346">Floor Cleaning</text>
    <text class="service" x="1072" y="376">Dry Carpet Cleaning</text>
    <text class="web" x="656" y="432">tolvcleaningco.com</text>
  </g>

  <g class="door-contact">
    <text class="brand" x="467" y="538" font-size="31" text-anchor="middle">TOLV</text>
    <text class="company" x="467" y="567" font-size="14" text-anchor="middle">TOLV CLEANING Co.</text>
    <text class="phone" x="467" y="588" text-anchor="middle">+974 5550 2143</text>
    <text class="phone" x="467" y="610" text-anchor="middle">+974 5550 8736</text>
  </g>

  <g class="service-photos">
    <circle class="photo-ring" cx="705" cy="525" r="56"/>
    <rect x="650" y="470" width="110" height="110" fill="url(#photo-carpet)" clip-path="url(#c1)" role="img" aria-label="Photo of a carpet cleaning machine on a carpet"/>
    <circle class="photo-ring" cx="855" cy="540" r="66"/>
    <rect x="790" y="475" width="130" height="130" fill="url(#photo-window)" clip-path="url(#c2)" role="img" aria-label="Photo of a cleaner in green uniform wiping a window"/>
    <circle class="photo-ring" cx="1010" cy="492" r="56"/>
    <rect x="955" y="437" width="110" height="110" fill="url(#photo-table)" clip-path="url(#c3)" role="img" aria-label="Photo of a hand dusting a table surface"/>
  </g>
</svg>
</body>
</html>
```